Business Card Design Project

the following info needs to fit nicely and professionally.

logo,office address,phone,fax,cell, email address,name, title.

example: attached logo, 48310 brenner ln suite 400 Calder Springs, CA 92178
p.858.317.2950, f.858.317.2958, c.858.264.7031
email. tomas@ridgeline-asphalt.com
name.tomas valcour
title. account manager

Target Market(s)

executives, ceo's, upper management

Industry/Entity Type

Business

```html
<!DOCTYPE html>
<html lang="en">
<head>
<meta charset="utf-8">
<title>Ridgeline Asphalt – Business Card</title>
<link rel="stylesheet" href="https://fonts.googleapis.com/css2?family=Cinzel:wght@400;600&family=Open+Sans:wght@600&display=swap">
<style>
  :root {
    --backdrop: #4a4a4a;
    --card-top: #6e0a0d;
    --card-mid: #3a0607;
    --card-bottom: #0b0303;
    --card-edge: rgba(255,255,255,0.18);
    --ink-light: #ffffff;
    --ink-soft: #e6dcdc;
    --gold: #f2b81c;
  }
  * { margin: 0; padding: 0; box-sizing: border-box; }
  html, body {
    width: 1200px; height: 456px; overflow: hidden;
    background: var(--backdrop);
  }
  .stage { position: relative; width: 1200px; height: 456px; }
  .card {
    position: absolute; top: 84px;
    width: 512px; height: 284px;
    border-radius: 26px;
    border: 1px solid var(--card-edge);
    background: linear-gradient(180deg, var(--card-top) 0%, var(--card-mid) 50%, var(--card-bottom) 100%);
    box-shadow: 0 6px 16px rgba(0,0,0,0.35);
    text-align: center;
    color: var(--ink-light);
  }
  .card--front { left: 73px; }
  .card--back { left: 616px; }

  .brand-wrap { position: absolute; left: 0; right: 0; text-align: center; }
  .card--front .brand-wrap { top: 138px; }
  .card--back .brand-wrap { top: 72px; }
  .brand { display: inline-flex; flex-direction: column; align-items: flex-end; }
  .brand__name {
    display: inline-flex; align-items: center; gap: 10px;
    font-family: "Cinzel", serif; font-weight: 400;
    color: var(--ink-light); letter-spacing: 0.5px; white-space: nowrap;
    line-height: 1.15;
  }
  .brand__dot { width: 12px; height: 12px; border-radius: 50%; background: var(--gold); }
  .card--front .brand__name { font-size: 31px; }
  .card--back .brand__name { font-size: 25px; }
  .brand__tagline {
    font-family: "Open Sans", sans-serif; font-weight: 600;
    color: var(--ink-light); white-space: nowrap;
  }
  .card--front .brand__tagline { font-size: 15px; margin-top: 2px; }
  .card--back .brand__tagline { font-size: 12px; }

  .person { position: absolute; top: 162px; left: 0; right: 0; font-family: "Cinzel", serif; color: var(--gold); }
  .person__name { font-size: 22px; font-weight: 600; letter-spacing: 0.5px; line-height: 1.1; }
  .person__title { font-size: 13px; letter-spacing: 1px; margin-top: 4px; }

  .contact {
    position: absolute; top: 220px; left: 0; right: 0;
    font-family: "Cinzel", serif; font-style: normal; font-size: 9.5px; line-height: 14.5px;
    color: var(--ink-soft); letter-spacing: 0.4px; white-space: nowrap;
  }
</style>
</head>
<body>
<main class="stage">
  <section class="card card--front" aria-label="Card front">
    <div class="brand-wrap">
      <div class="brand">
        <span class="brand__name"><span class="brand__dot"></span>RIDGELINE ASPHALT</span>
        <span class="brand__tagline">Service Before All Else</span>
      </div>
    </div>
  </section>

  <section class="card card--back" aria-label="Card back">
    <div class="brand-wrap">
      <div class="brand">
        <span class="brand__name"><span class="brand__dot"></span>RIDGELINE ASPHALT</span>
        <span class="brand__tagline">Service Before All Else</span>
      </div>
    </div>
    <div class="person">
      <p class="person__name">Tomas Valcour</p>
      <p class="person__title">ACCOUNT MANAGER</p>
    </div>
    <address class="contact">
      <p>48310 BRENNER LN SUITE 400 CALDER SPRINGS, CA 92178</p>
      <p>P. 858.317.2950 &nbsp;F. 858.317.2958 &nbsp;C. 858.264.7031</p>
      <p>EMAIL. tomas@ridgeline-asphalt.com</p>
    </address>
  </section>
</main>
</body>
</html>
```